Fitness Training academy needs a business card design

We need a business card design for a NEW business that teaches/trains people how to become personal trainers. We would like to see designs both with and without our QR code. We would like our designs double sided.

See the following attachments
Design Brief
Logos (both black background, white background in all formats)
QR Code

Industry/Entity Type

Business

```html
<!DOCTYPE html>
<html lang="en">
<head>
<meta charset="utf-8">
<title>Riseforce Academy – Business Card</title>
<link rel="stylesheet" href="https://fonts.googleapis.com/css2?family=Open+Sans:wght@300;400;600;700&display=swap">
<style>
  :root {
    --backdrop: #e9e6e1;
    --card-top: #2b2b2d;
    --card-bottom: #0b0b0c;
    --ink-light: #f2f2f2;
    --ink-muted: #a9a9ab;
    --brand-orange: #f0702a;
    --strip-red: #d8203a;
    --strip-orange: #ee6a2a;
    --strip-yellow: #f4b21e;
    --rule: #4a4a4d;
  }
  * { box-sizing: border-box; margin: 0; padding: 0; }
  html, body { width: 1200px; height: 1023px; overflow: hidden; }
  body {
    background: var(--backdrop);
    font-family: "Open Sans", Arial, sans-serif;
    position: relative;
  }
  .card {
    position: absolute;
    left: 220px;
    width: 760px;
    height: 434px;
    border-radius: 6px;
    background: linear-gradient(160deg, var(--card-top) 0%, #161617 55%, var(--card-bottom) 100%);
    box-shadow: 0 14px 30px rgba(0,0,0,0.28);
    overflow: hidden;
    color: var(--ink-light);
  }
  .card--front { top: 52px; }
  .card--back { top: 537px; }

  /* brand name */
  .brand { display: flex; align-items: center; gap: 14px; }
  .brand__dot {
    width: 30px; height: 30px; border-radius: 50%;
    background: var(--brand-orange);
    flex: none;
  }
  .brand__name {
    font-weight: 600;
    font-size: 28px;
    color: var(--ink-light);
    line-height: 1;
    white-space: nowrap;
  }

  /* front */
  .card--front .brand-block { position: absolute; left: 48px; top: 78px; }
  .holder { position: absolute; left: 48px; bottom: 74px; }
  .holder__name { font-size: 28px; font-weight: 700; line-height: 1.2; }
  .holder__title { margin-top: 4px; font-size: 16px; color: var(--ink-muted); }

  .contact { position: absolute; left: 470px; top: 64px; width: 250px; }
  .contact__address { font-size: 15px; line-height: 1.45; color: var(--ink-muted); }
  .contact__rule { height: 1px; background: var(--rule); margin: 18px 0 16px; }
  .contact__list { list-style: none; }
  .contact__item {
    display: flex; align-items: center; gap: 12px;
    font-size: 15px; color: var(--ink-muted);
    line-height: 1; margin-bottom: 12px;
    white-space: nowrap;
  }
  .contact__icon { width: 16px; height: 16px; flex: none; }

  .accent-strip {
    position: absolute; left: 0; right: 0; bottom: 0; height: 22px;
    background: linear-gradient(90deg, var(--strip-red) 0%, var(--strip-orange) 45%, var(--strip-yellow) 70%, var(--strip-orange) 85%, var(--strip-red) 100%);
  }
  .accent-strip__notch {
    position: absolute; left: 420px; top: -9px;
    width: 0; height: 0;
    border-left: 9px solid transparent;
    border-right: 9px solid transparent;
    border-bottom: 9px solid var(--strip-yellow);
  }

  /* back */
  .social {
    position: absolute; left: 44px; top: 60px; bottom: 60px;
    display: flex; gap: 18px;
  }
  .social__icons { display: flex; flex-direction: column; gap: 12px; }
  .social__tile { width: 26px; height: 26px; border-radius: 3px; }
  .social__tile--blue { background: #3b5a98; }
  .social__tile--sky { background: #2aa3e0; }
  .social__tile--grey { background: #8a8a8c; }
  .social__tile--red { background: #d43d3d; }
  .social__divider { width: 1px; background: var(--rule); }
  .social__handle {
    writing-mode: vertical-rl;
    transform: rotate(180deg);
    font-size: 14px; font-weight: 300; color: var(--ink-muted);
    letter-spacing: 0.5px;
  }
  .card--back .brand-block { position: absolute; left: 270px; top: 200px; }
  .back-rule {
    position: absolute; left: 130px; right: 44px; bottom: 40px;
    height: 1px; background: var(--rule);
  }
</style>
</head>
<body>

<section class="card card--front" aria-label="Business card front">
  <div class="brand-block">
    <div class="brand">
      <span class="brand__dot"></span>
      <span class="brand__name">Riseforce Academy</span>
    </div>
  </div>

  <div class="holder">
    <div class="holder__name">Jordan (Jo) Mercer</div>
    <div class="holder__title">Managing Director</div>
  </div>

  <div class="contact">
    <p class="contact__address">PO Box 4120<br>Harbourside Qld 4305</p>
    <div class="contact__rule"></div>
    <ul class="contact__list">
      <li class="contact__item">
        <svg class="contact__icon" viewBox="0 0 16 16"><rect x="4" y="1" width="8" height="14" rx="1.5" fill="none" stroke="#a9a9ab" stroke-width="1.4"/><circle cx="8" cy="12.5" r="0.9" fill="#a9a9ab"/></svg>
        0400 123 456
      </li>
      <li class="contact__item">
        <svg class="contact__icon" viewBox="0 0 16 16"><path d="M3 2h3l1.5 3.5-2 1.2a8 8 0 0 0 3.8 3.8l1.2-2L14 10v3a1 1 0 0 1-1 1A11 11 0 0 1 2 3a1 1 0 0 1 1-1z" fill="#a9a9ab"/></svg>
        1300 00 12 34
      </li>
      <li class="contact__item">
        <svg class="contact__icon" viewBox="0 0 16 16"><rect x="1" y="3" width="14" height="10" rx="1" fill="none" stroke="#a9a9ab" stroke-width="1.4"/><path d="M1.5 3.5 8 9l6.5-5.5" fill="none" stroke="#a9a9ab" stroke-width="1.4"/></svg>
        jmercer@rfa-mail.com.au
      </li>
      <li class="contact__item">
        <svg class="contact__icon" viewBox="0 0 16 16"><circle cx="8" cy="8" r="6.5" fill="none" stroke="#a9a9ab" stroke-width="1.3"/><path d="M1.5 8h13M8 1.5c-3 3.5-3 9.5 0 13M8 1.5c3 3.5 3 9.5 0 13" fill="none" stroke="#a9a9ab" stroke-width="1.1"/></svg>
        www.rfa-mail.com.au
      </li>
    </ul>
  </div>

  <div class="accent-strip"><span class="accent-strip__notch"></span></div>
</section>

<section class="card card--back" aria-label="Business card back">
  <div class="social">
    <div class="social__icons">
      <span class="social__tile social__tile--blue"></span>
      <span class="social__tile social__tile--sky"></span>
      <span class="social__tile social__tile--grey"></span>
      <span class="social__tile social__tile--red"></span>
    </div>
    <div class="social__divider"></div>
    <span class="social__handle">/riseforceacademy</span>
  </div>

  <div class="brand-block">
    <div class="brand">
      <span class="brand__dot"></span>
      <span class="brand__name">Riseforce Academy</span>
    </div>
  </div>

  <div class="back-rule"></div>
</section>

</body>
</html>
```